Organic loose leaf tea labels hand crafted on the Great Ocean Road

We are two mums that hand craft organic loose leaf tea in our spare time. . . We are starting to get a lovely following of cafes but need to work on our retail market. We have black boxes that have our logo and name in foiled gold on the front. WE would like each tea label in a different back ground colour so that the tea is easier to identify, whilst the back label to be black background with gold text.
We are after two base labels for our new tea boxes, one label for the front with the tea name, a brief description and the ingredients. Whilst the back label needs to have information on how to make the tea, place for barcode, weight and best before. I have uploaded a file below with more detailed description.
Our box dimensions are 16cm high and 8cm across the front/back
We also need to update our business cards to reflect the new direction, moving away from the 'kraft' look. our website is www.brewandwhisper.com.au

Target Market(s)

women aged 25-45

Industry/Entity Type

Font styles to use
Other font styles liked:
• We use 'Subway Novella'

Requirements
Must have
• Minimalist feel - easy to read

```html
<!DOCTYPE html>
<html lang="en">
<head>
<meta charset="utf-8">
<title>brew &amp; whisper — tea box fronts</title>
<link rel="stylesheet" href="https://fonts.googleapis.com/css2?family=Arvo:wght@400;700&family=Open+Sans:wght@400;600&display=swap">
<style>
  :root {
    --canvas: #e9e9e7;
    --box-dark: #0c0c0c;
    --box-mid: #262626;
    --gold: #c9a536;
    --label-white: #ffffff;
    --breakfast: #6f9a72;
    --breakfast-ink: #5e8a63;
    --mint: #3fcf96;
    --mint-ink: #2fbf86;
    --citrus: #f7e184;
    --citrus-ink: #b59a2f;
    --slab: "Arvo", Georgia, serif;
    --body: "Open Sans", Arial, sans-serif;
  }
  * { box-sizing: border-box; margin: 0; padding: 0; }
  html, body { width: 1200px; height: 880px; overflow: hidden; }
  body { background: var(--canvas); position: relative; }

  .tea-box {
    position: absolute;
    top: 166px;
    width: 264px;
    height: 535px;
    background: linear-gradient(90deg, var(--box-dark) 0%, var(--box-mid) 45%, #1a1a1a 60%, var(--box-dark) 100%);
  }
  .tea-box--breakfast { left: 149px; }
  .tea-box--mint { left: 473px; }
  .tea-box--citrus { left: 796px; }

  .brand {
    position: absolute;
    top: 52px;
    left: 0;
    width: 100%;
    text-align: center;
  }
  .brand__dot {
    display: block;
    width: 18px;
    height: 18px;
    margin: 0 auto 8px;
    border-radius: 50%;
    background: var(--gold);
  }
  .brand__name {
    font-family: var(--slab);
    font-weight: 700;
    font-size: 27px;
    line-height: 1.0;
    color: var(--gold);
  }
  .tagline {
    position: absolute;
    top: 170px;
    left: 0;
    width: 100%;
    text-align: center;
    font-family: var(--slab);
    font-weight: 700;
    font-size: 10.5px;
    color: var(--gold);
  }

  .label {
    position: absolute;
    top: 273px;
    left: 44px;
    width: 175px;
    height: 174px;
    background: var(--label-white);
    border-radius: 4px;
    padding: 9px;
  }
  .label__field {
    position: relative;
    width: 100%;
    height: 100%;
  }
  .label__pattern {
    position: absolute;
    inset: 0;
  }
  .label--breakfast .label__pattern { background: var(--breakfast); }
  .label--mint .label__pattern { background: var(--mint); }
  .label--citrus .label__pattern { background: var(--citrus); }

  .label__medallion {
    position: absolute;
    left: 50%;
    top: 50%;
    width: 142px;
    height: 142px;
    transform: translate(-50%, -50%);
    border-radius: 50%;
    background: var(--label-white);
    border: 3px double currentColor;
    display: flex;
    flex-direction: column;
    align-items: center;
    justify-content: center;
    text-align: center;
    padding: 0 18px;
  }
  .label--breakfast .label__medallion { color: var(--breakfast-ink); }
  .label--mint .label__medallion { color: var(--mint-ink); }
  .label--citrus .label__medallion { color: var(--citrus-ink); }

  .label__name {
    font-family: var(--slab);
    font-weight: 700;
    font-size: 17px;
    line-height: 1.05;
    margin-bottom: 4px;
  }
  .label__desc {
    font-family: var(--body);
    font-size: 6.4px;
    line-height: 1.4;
  }
</style>
</head>
<body>

  <section class="tea-box tea-box--breakfast">
    <div class="brand"><span class="brand__dot"></span><div class="brand__name">brew &amp;<br>whisper</div></div>
    <p class="tagline">hand crafted organic loose leaf tea</p>
    <div class="label label--breakfast">
      <div class="label__field">
        <div class="label__pattern" role="img" aria-label="Sage green decorative tile pattern"></div>
        <div class="label__medallion">
          <h2 class="label__name">English<br>Breakfast</h2>
          <p class="label__desc">A bold morning brew with a rich, malty body that stands up well to milk. Ingredients: Assam &amp; Ceylon black tea</p>
        </div>
      </div>
    </div>
  </section>

  <section class="tea-box tea-box--mint">
    <div class="brand"><span class="brand__dot"></span><div class="brand__name">brew &amp;<br>whisper</div></div>
    <p class="tagline">hand crafted organic loose leaf tea</p>
    <div class="label label--mint">
      <div class="label__field">
        <div class="label__pattern" role="img" aria-label="Mint green decorative tile pattern"></div>
        <div class="label__medallion">
          <h2 class="label__name">Moroccan<br>Mint</h2>
          <p class="label__desc">Bright gunpowder green tea with a cool, sweet herbal finish. Ingredients: Green tea, mint leaves &amp; lemon balm</p>
        </div>
      </div>
    </div>
  </section>

  <section class="tea-box tea-box--citrus">
    <div class="brand"><span class="brand__dot"></span><div class="brand__name">brew &amp;<br>whisper</div></div>
    <p class="tagline">hand crafted organic loose leaf tea</p>
    <div class="label label--citrus">
      <div class="label__field">
        <div class="label__pattern" role="img" aria-label="Pale yellow decorative tile pattern"></div>
        <div class="label__medallion">
          <h2 class="label__name">Citrus<br>Dawn</h2>
          <p class="label__desc">A gentle zesty infusion with a soft, warming glow. Ingredients: Lemon peel, orange zest, ginger, aniseed &amp; lemon myrtle</p>
        </div>
      </div>
    </div>
  </section>

</body>
</html>
```